Corporate Web Design

Hello Designers,
Thank you for wanting to participate in designing a web design.
First off let me introduce ourselves, we are a precious metals refinery that is base in the west coast. Our Name is Harborline Precious Metals Refinery. Our sole goal for this website is simplicity yet cleanliness and elegance. We want to demonstrate the process and procedures of what we do and who we are.
The Lay out:
We want about 4-5 Tabs that will help guide our customers through our website with ease. Some ideas of what we want to call the tabs might be….
1. Home
- This tab will take them to the home page
2. Contact Us
- Our contact information
- Client contact form
- Some sort of membership form?
3. Pick-up Service
- This tab will explain how this process works and what it in tells.
- This page will also have a section for requirements.
- This pickup service will only be available for members and people that have a good account with us.
4. How it Works
- This page will explain who we are and how we work.
- I would like to somehow creatively show the process and the steps we take in melting their gold.
Effects:
An effect that I would want to see is a live precious metal stock price. This price will automatically update and post the most recent and current price on the market of what the gold, silver etc prices. Here is a link of a company that has something similar, http://kelvaro-refining.example/ what I like about this spot price pop up, is that it follows them all over the page. I like that idea.
I would also like some sort of slide show that has videos and demonstrations of our company and business.
These are all Websites of our competitors that we like many ideas from.
http://www.hlpmr.example/
What we like about this website is the tab that says “Request Pick-up” With a form that they have to fill out. We would want more than just a form; we would want some sort of membership application.
http://dovemetals.example/
What I like about this website is the slideshow. It’s very simple yet professional. This is something that I would like to incorporate into our website. I also like the live metal market price.
http://kelvaro-refining.example/
This is another example of a website that has a live spot price of the gold market. I like how the gold price follows you around the page. I would like to see some of your ideas with this.
http://www.quillmetals.example/
This website is very clean and simple. I like the colors. I would like a little more character than what they have but I like the simplicity.
The colors we like are black, white, silver, gold, Royal Blue etc; basically anything that creates a clean atmosphere. These colors match our logo and also have a very elegant and professional perception to them. Please do not limit yourselves to only our suggestions
These are links to our Logo with all different colors.
https://www.filecrate.example/s/a11b22c33d44e55/LOGO_black_background.png
https://www.filecrate.example/s/f66g77h88i99j00/LOGO_black.png
https://www.filecrate.example/s/k12l34m56n78o90/LOGO_transparent_background.png
https://www.filecrate.example/s/p21q43r65s87t09/LOGO_white_background.png
These are links to a brochure of our business that represents and shows the process of what we do and demonstrates who we are.
https://www.filecrate.example/s/u13v35w57x79y91/inside_1.pdf
https://www.filecrate.example/s/z24a46b68c80d02/inside_2.pdf
Bottom line we want to see examples of ideas and layouts that you have for a website. Please upload them and We will comment back on them.

```html
<!DOCTYPE html>
<html lang="en">
<head>
<meta charset="utf-8">
<title>Harborline Precious Metals Refinery – Web Design</title>
<link rel="stylesheet" href="https://fonts.googleapis.com/css2?family=PT+Sans:wght@400;700&family=PT+Sans+Narrow:wght@400;700&display=swap">
<style>
  :root{
    --stage:#f1f1f1;
    --paper:#ffffff;
    --ticker:#2b333d;
    --ticker-line:#56606b;
    --gold:#f3b51d;
    --royal:#1f5bc4;
    --ink:#2a2a2a;
    --muted:#8a8a8a;
    --hero-yellow:#ffd51a;
    --icon-grey:#a7a7a7;
    --icon-navy:#1e3a7a;
    --icon-cyan:#1cb5ea;
    --icon-blue:#1735d6;
    --icon-deep:#1c336e;
    --orange:#f7941d;
    --wordmark:#a88b45;
  }
  *{box-sizing:border-box;margin:0;padding:0}
  html,body{width:1200px;height:1067px;overflow:hidden}
  body{background:var(--stage);font-family:"PT Sans",sans-serif;color:var(--ink);position:relative}
  a{text-decoration:none}

  /* ---------- Home page ---------- */
  .home{position:absolute;left:40px;top:214px;width:640px;height:640px;background:var(--paper);box-shadow:0 2px 14px rgba(0,0,0,.08)}
  .ticker{display:flex;height:45px;background:var(--ticker);color:#fff;font-size:9px;position:relative}
  .ticker__metal{width:88px;background:var(--gold);padding:7px 8px;color:#fff}
  .ticker__metal small{display:block;font-size:7px;opacity:.9}
  .ticker__select{display:inline-block;margin-top:4px;background:rgba(255,255,255,.35);border-radius:8px;padding:1px 8px;font-size:8px;font-weight:700}
  .ticker__cell{padding:7px 10px;text-align:center;border-right:1px dotted var(--ticker-line);display:flex;flex-direction:column;justify-content:center}
  .ticker__cell small{font-size:7px;color:#c8cdd3}
  .ticker__cell b{font-size:10px;font-weight:700;margin-top:3px}
  .ticker__pair{display:flex;gap:16px}
  .ticker__update{width:150px}
  .ticker__refresh{margin-left:auto;border-right:0;font-size:7px;font-weight:700;letter-spacing:.5px}
  .ticker__handle{position:absolute;left:303px;top:45px;width:34px;height:13px;background:var(--ticker);border-radius:0 0 5px 5px;display:flex;flex-direction:column;align-items:center;justify-content:center;gap:2px}
  .ticker__handle i{display:block;width:14px;height:1px;background:#fff}

  .brand{position:absolute;right:24px;top:58px;font-size:14px;letter-spacing:1px;color:var(--wordmark);font-weight:400;white-space:nowrap}

  .nav{display:flex;justify-content:center;gap:34px;margin-top:40px;height:62px}
  .nav__item{text-align:center;width:92px;font-size:9.5px;font-weight:700;text-transform:uppercase;color:var(--ink);position:relative;white-space:nowrap}
  .nav__item svg{display:block;margin:0 auto 6px;width:16px;height:16px}
  .nav__item small{display:block;font-size:7.5px;font-weight:400;text-transform:none;color:var(--muted);margin-top:2px}
  .nav__item--active::after{content:"";position:absolute;left:12px;right:12px;bottom:-4px;height:3px;background:var(--royal)}

  .hero{position:relative;height:272px;margin-top:6px;overflow:hidden}
  .hero__photo{position:absolute;inset:0;background:linear-gradient(90deg,#d8dde3 0%,#3f5aa8 30%,#9aa6bd 55%,#cdb6a2 75%,#c98f3a 100%)}
  .hero__caption{position:absolute;left:88px;top:0;bottom:0;width:300px;background:rgba(40,44,60,.28);padding:50px 0 0 14px}
  .hero__title{font-family:"PT Sans Narrow",sans-serif;color:var(--hero-yellow);font-size:40px;line-height:40px;font-weight:400}
  .hero__sub{font-family:"PT Sans Narrow",sans-serif;color:#fff;font-size:25px;margin-top:10px}
  .hero__arrow{position:absolute;top:126px;width:0;height:0;border-top:9px solid transparent;border-bottom:9px solid transparent}
  .hero__arrow--prev{left:26px;border-right:12px solid rgba(255,255,255,.8)}
  .hero__arrow--next{right:6px;border-left:12px solid rgba(255,255,255,.8)}
  .hero__dots{position:absolute;left:305px;bottom:14px;display:flex;gap:10px}
  .hero__dots i{width:9px;height:9px;border-radius:50%;background:rgba(40,40,40,.45)}
  .hero__dots i.is-on{background:var(--hero-yellow)}

  .values{display:flex;justify-content:center;gap:30px;padding-top:50px;padding-left:40px}
  .value{width:86px;text-align:center;font-size:10.5px;color:var(--ink);line-height:13px}
  .value__disc{width:84px;height:84px;border-radius:50%;display:flex;align-items:center;justify-content:center;margin:0 auto 10px}
  .value__disc svg{width:40px;height:40px}

  /* ---------- How it works page ---------- */
  .works{position:absolute;left:720px;top:214px;width:440px;height:594px;background:var(--paper);box-shadow:0 2px 14px rgba(0,0,0,.08);padding:0 26px}
  .works .ticker__handle{left:203px;top:0}
  .works .brand{top:26px;right:20px;font-size:11px}
  .works .nav{margin-top:60px;gap:18px;height:46px}
  .works .nav__item{width:68px;font-size:7px}
  .works .nav__item svg{width:12px;height:12px;margin-bottom:4px}
  .works .nav__item small{font-size:5.5px}
  .works .nav__item--active::after{bottom:-2px;height:2px;left:14px;right:14px}
  .works__title{font-family:"PT Sans Narrow",sans-serif;font-size:29px;font-weight:400;margin-top:26px;color:var(--ink)}
  .works__intro{font-size:8px;line-height:10px;color:#444;margin-top:6px}
  .steps{display:flex;gap:30px;margin-top:18px;padding-left:4px}
  .steps__thumb{width:74px;height:74px;border-radius:50%;background:radial-gradient(circle,#c9c9c9,#6d6d6d)}
  .steps__thumb--active{background:radial-gradient(circle,#e1c27a,#8b6a2c)}
  .step{display:flex;margin-top:18px;height:250px}
  .step__photo{flex:0 0 250px;background:linear-gradient(135deg,#5b5148 0%,#b08c45 45%,#d9b45a 70%,#6a6058 100%)}
  .step__panel{flex:1;background:var(--orange);color:#fff;padding:20px 14px}
  .step__title{font-family:"PT Sans Narrow",sans-serif;font-size:40px;font-weight:400;line-height:40px}
  .step__text{font-size:8px;line-height:11px;margin-top:14px}
</style>
</head>
<body>

<section class="home" aria-label="Home page">
  <div class="ticker">
    <div class="ticker__metal"><small>Real-time Price</small><span class="ticker__select">Gold ▾</span></div>
    <div class="ticker__cell ticker__update"><small>Last Update</small><b>Fri May 31, 4:21 AM CDT</b></div>
    <div class="ticker__cell"><div class="ticker__pair"><span><small>Bid</small><br><b>1,413.02</b></span><span><small>Ask</small><br><b>1,413.24</b></span></div></div>
    <div class="ticker__cell"><div class="ticker__pair"><span><small>Low</small><br><b>1,411.86</b></span><span><small>High</small><br><b>1,421.86</b></span></div></div>
    <div class="ticker__cell"><small>Change</small><b>-0.49(-0.03%)</b></div>
    <div class="ticker__cell ticker__refresh">REFRESH<br><svg width="12" height="12" viewBox="0 0 12 12" style="margin:4px auto 0"><g stroke="#fff" stroke-width="1.4" stroke-linecap="round"><line x1="6" y1="1" x2="6" y2="3"/><line x1="6" y1="9" x2="6" y2="11"/><line x1="1" y1="6" x2="3" y2="6"/><line x1="9" y1="6" x2="11" y2="6"/><line x1="2.5" y1="2.5" x2="3.9" y2="3.9"/><line x1="8.1" y1="8.1" x2="9.5" y2="9.5"/><line x1="2.5" y1="9.5" x2="3.9" y2="8.1"/><line x1="8.1" y1="3.9" x2="9.5" y2="2.5"/></g></svg></div>
    <div class="ticker__handle"><i></i><i></i></div>
  </div>

  <div class="brand">Harborline Refinery</div>

  <nav class="nav">
    <a class="nav__item nav__item--active"><svg viewBox="0 0 16 16"><path d="M8 1 1 7.5h2V15h4v-4h2v4h4V7.5h2z" fill="#222"/></svg>Home<small>welcome</small></a>
    <a class="nav__item"><svg viewBox="0 0 16 16"><rect x="1.5" y="1.5" width="13" height="13" fill="none" stroke="#222" stroke-dasharray="2 1.5"/><path d="M8 4 5 8h2v4h2V8h2z" fill="#222"/></svg>Pick-up Service<small>section requirements</small></a>
    <a class="nav__item"><svg viewBox="0 0 16 16"><circle cx="5.5" cy="5.5" r="3.2" fill="none" stroke="#222" stroke-width="2"/><circle cx="11" cy="11" r="2.6" fill="none" stroke="#222" stroke-width="2"/></svg>How it Works<small>flow &amp; process</small></a>
    <a class="nav__item"><svg viewBox="0 0 16 16"><rect x="1" y="3" width="14" height="10" fill="#222"/><path d="M1 3l7 6 7-6" fill="none" stroke="#fff" stroke-width="1.2"/></svg>Contact Us<small>keep in touch</small></a>
  </nav>

  <div class="hero">
    <div class="hero__photo" role="img" aria-label="Refinery worker in protective gloves stirring molten gold in a crucible"></div>
    <div class="hero__caption">
      <h1 class="hero__title">We are a precious<br>metals refinery</h1>
      <p class="hero__sub">that is base in the west coast.</p>
    </div>
    <span class="hero__arrow hero__arrow--prev"></span>
    <span class="hero__arrow hero__arrow--next"></span>
    <div class="hero__dots"><i class="is-on"></i><i></i><i></i><i></i></div>
  </div>

  <div class="values">
    <div class="value"><div class="value__disc" style="background:var(--icon-grey)"><svg viewBox="0 0 40 40" fill="#fff"><circle cx="20" cy="11" r="4"/><rect x="16" y="16" width="8" height="16" rx="2"/><circle cx="11" cy="14" r="3"/><rect x="8" y="18" width="6" height="12" rx="2"/><circle cx="29" cy="14" r="3"/><rect x="26" y="18" width="6" height="12" rx="2"/></svg></div>Transparency</div>
    <div class="value"><div class="value__disc" style="background:var(--icon-navy)"><svg viewBox="0 0 40 40" fill="none" stroke="#fff" stroke-width="2.5"><circle cx="20" cy="21" r="12"/><circle cx="20" cy="21" r="6"/><path d="M20 21 31 10M27 9h5v5"/></svg></div>Accuracy</div>
    <div class="value"><div class="value__disc" style="background:var(--icon-cyan)"><svg viewBox="0 0 40 40" fill="none" stroke="#fff" stroke-width="2.5"><path d="M7 27a13 13 0 1 1 26 0z"/><path d="M20 26 26 16"/><path d="M11 21h2M27 21h2M20 12v2" stroke-width="1.6"/></svg></div>One Day<br>Settlements</div>
    <div class="value"><div class="value__disc" style="background:var(--icon-blue)"><svg viewBox="0 0 40 40"><circle cx="17" cy="13" r="6" fill="#fff"/><path d="M6 32c0-8 5-12 11-12s9 3 10 6v6z" fill="#fff"/><circle cx="29" cy="28" r="7" fill="#fff" stroke="var(--icon-blue)" stroke-width="2"/><text x="29" y="32" font-size="10" font-weight="700" text-anchor="middle" fill="var(--icon-blue)" font-family="PT Sans, sans-serif">$</text></svg></div>Cash<br>Payment</div>
    <div class="value"><div class="value__disc" style="background:var(--icon-deep)"><svg viewBox="0 0 40 40" fill="none" stroke="#fff" stroke-width="2"><rect x="8" y="10" width="24" height="18"/><path d="M12 15h10M12 19h8M12 23h6"/><circle cx="27" cy="22" r="3" fill="#fff"/><path d="M25 25l-1 6 3-2 3 2-1-6"/></svg></div>Trust</div>
  </div>
</section>

<section class="works" aria-label="How it works page">
  <div class="ticker__handle"><i></i><i></i></div>
  <div class="brand">Harborline Refinery</div>

  <nav class="nav">
    <a class="nav__item"><svg viewBox="0 0 16 16"><path d="M8 1 1 7.5h2V15h4v-4h2v4h4V7.5h2z" fill="#222"/></svg>Home<small>welcome</small></a>
    <a class="nav__item"><svg viewBox="0 0 16 16"><rect x="1.5" y="1.5" width="13" height="13" fill="none" stroke="#222" stroke-dasharray="2 1.5"/><path d="M8 4 5 8h2v4h2V8h2z" fill="#222"/></svg>Pick-up Service<small>section requirements</small></a>
    <a class="nav__item nav__item--active"><svg viewBox="0 0 16 16"><circle cx="5.5" cy="5.5" r="3.2" fill="none" stroke="#222" stroke-width="2"/><circle cx="11" cy="11" r="2.6" fill="none" stroke="#222" stroke-width="2"/></svg>How it Works<small>flow &amp; process</small></a>
    <a class="nav__item"><svg viewBox="0 0 16 16"><rect x="1" y="3" width="14" height="10" fill="#222"/><path d="M1 3l7 6 7-6" fill="none" stroke="#fff" stroke-width="1.2"/></svg>Contact Us<small>keep in touch</small></a>
  </nav>

  <h2 class="works__title">HOW IT WORKS ?</h2>
  <p class="works__intro">We receive your scrap gold, silver and platinum, log every piece in front of you, and guide each lot through weighing, melting, assay and settlement. Every step is recorded so you can follow your metal from the counter to the final payment.</p>

  <div class="steps">
    <div class="steps__thumb steps__thumb--active" role="img" aria-label="Step 1: sorting gold jewellery"></div>
    <div class="steps__thumb" role="img" aria-label="Step 2: weighing the metal"></div>
    <div class="steps__thumb" role="img" aria-label="Step 3: melting in the furnace"></div>
    <div class="steps__thumb" role="img" aria-label="Step 4: assay and settlement"></div>
  </div>

  <div class="step">
    <div class="step__photo" role="img" aria-label="Hands sorting a pile of gold jewellery on a tray"></div>
    <div class="step__panel">
      <h3 class="step__title">STEP 1</h3>
      <p class="step__text">Bring your items to our counter or book a pickup. A specialist sorts each piece by metal and karat, removes stones and non-metal parts, and records the gross weight with you present before melting begins.</p>
    </div>
  </div>
</section>

</body>
</html>
```